Thornwick auto buffing and headlight restoration

I'm offering a service the will restore dull and discoloured headlights caused by sun damage. I also want to offer minor scratch repairs. $25 per headlight $10-$30 for scratches Mobile serviceI'd like to have an example of a dull and a new headlight. Clean colours eg. Blues,silver and whites.Very clean uncomplicated and professionals looking card. I'd like it to have a bold logo.

Target Market(s)

All car, truck and vehicle owners. Automotive industries.

Industry/Entity Type

Automotive

Contact Information for Business Card

(Front)
Headlight restoration and scratch Repair
Callum Thornwick
Mobile-0412 386 904
(Back)
Pricing
$25 per headlight
$10-$35 per scratch

Font styles to use
Sans Serif

Colors
85cae6
ffffff
0355a3
faa54b

Requirements
Must have
• Logo
• I would like my name to look confident. As if to say "Clearbeam Auto"
• Bold easy to read text
• Clean lines
• Name -Callum Thornwick
• Phone- txt or call 0412386904
• Email- 47calt@mailverno.com
Nice to have
• I'm open to other color schemes
• 4 color scheme only
• Minimal orange
• Small amount of Silver if possible
• Bold outlined logo
Should not have
• Complex lines and logos

```html
<!DOCTYPE html>
<html lang="en">
<head>
<meta charset="utf-8">
<title>Clearbeam Auto – Business Cards</title>
<link rel="stylesheet" href="https://fonts.googleapis.com/css2?family=Orbitron:wght@500;700;900&display=swap">
<style>
  :root {
    --blue: #0355a3;
    --sky: #85cae6;
    --orange: #faa54b;
    --white: #ffffff;
    --stage: #e9ecef;
  }
  * { margin: 0; padding: 0; box-sizing: border-box; }
  html, body { width: 1200px; height: 800px; overflow: hidden; }
  body {
    background: var(--stage);
    font-family: "Orbitron", sans-serif;
    display: flex;
    align-items: center;
    justify-content: center;
    gap: 40px;
  }
  .card {
    width: 540px;
    height: 310px;
    position: relative;
    overflow: hidden;
    box-shadow: 0 6px 18px rgba(0,0,0,0.18);
  }

  /* Front */
  .card-front { background: var(--white); }
  .front-top-strip { height: 16px; background: var(--orange); }
  .front-brand {
    height: 86px;
    padding: 10px 26px 0;
  }
  .brand-name {
    font-weight: 900;
    font-size: 38px;
    letter-spacing: 2px;
    text-transform: uppercase;
    color: var(--orange);
    line-height: 1.1;
  }
  .brand-tagline {
    font-weight: 500;
    font-size: 11.5px;
    letter-spacing: 1.2px;
    text-transform: uppercase;
    color: var(--blue);
    margin-top: 6px;
  }
  .front-name-band {
    height: 40px;
    background: var(--orange);
    display: flex;
    align-items: center;
    padding-left: 26px;
  }
  .owner-name {
    font-weight: 700;
    font-size: 24px;
    letter-spacing: 2px;
    text-transform: uppercase;
    color: var(--white);
  }
  .front-contact {
    height: 154px;
    background: var(--blue);
    position: relative;
  }
  .contact-item {
    position: absolute;
    display: flex;
    align-items: center;
    gap: 12px;
    color: var(--white);
    font-weight: 500;
    font-size: 13px;
    letter-spacing: 1px;
    text-transform: uppercase;
  }
  .contact-phone { left: 26px; top: 28px; }
  .contact-email { right: 26px; bottom: 30px; flex-direction: row-reverse; }
  .contact-icon { width: 46px; height: 46px; flex: none; }
  .front-bottom-strip { height: 14px; background: var(--white); }

  /* Back */
  .card-back {
    background: linear-gradient(100deg, var(--blue) 0%, var(--blue) 52%, #3b7fbf 78%, var(--sky) 100%);
    color: var(--white);
  }
  .back-streak {
    position: absolute;
    left: 60px;
    right: 60px;
    top: 102px;
    height: 44px;
    background: linear-gradient(90deg, rgba(255,255,255,0) 0%, rgba(255,255,255,0.18) 20%, rgba(255,255,255,0.18) 80%, rgba(255,255,255,0) 100%);
  }
  .back-brand {
    position: absolute;
    left: 0; right: 0;
    top: 104px;
    text-align: center;
    font-weight: 900;
    font-size: 32px;
    letter-spacing: 2px;
    text-transform: uppercase;
    color: var(--white);
  }
  .pricing {
    position: absolute;
    left: 0; right: 0;
    top: 182px;
    text-align: center;
    text-transform: uppercase;
    font-weight: 500;
    letter-spacing: 1px;
  }
  .pricing-title { font-size: 16px; margin-bottom: 6px; }
  .pricing-line { font-size: 13px; line-height: 1.5; }
</style>
</head>
<body>

  <article class="card card-front">
    <div class="front-top-strip"></div>
    <header class="front-brand">
      <div class="brand-name">Clearbeam Auto</div>
      <div class="brand-tagline">Headlight restoration and scratch repair</div>
    </header>
    <div class="front-name-band">
      <div class="owner-name">Callum Thornwick</div>
    </div>
    <section class="front-contact">
      <div class="contact-item contact-phone">
        <svg class="contact-icon" viewBox="0 0 46 46" aria-hidden="true">
          <circle cx="23" cy="23" r="20" fill="none" stroke="#fff" stroke-width="2.5"/>
          <path d="M16 14 l4 -1 l3 6 l-2.5 2 q2 4.5 6 6.5 l2 -2.5 l6 3 l-1 4 q-2 2 -5 1 q-10 -4 -13.5 -14 q-1 -3 1 -5z" fill="#fff"/>
        </svg>
        <span>0412386904</span>
      </div>
      <div class="contact-item contact-email">
        <svg class="contact-icon" viewBox="0 0 46 46" aria-hidden="true">
          <circle cx="23" cy="23" r="20" fill="none" stroke="#fff" stroke-width="2.5"/>
          <rect x="13" y="16" width="20" height="14" fill="#fff"/>
          <path d="M13 16 L23 24 L33 16" fill="none" stroke="#0355a3" stroke-width="1.8"/>
        </svg>
        <span>47calt@mailverno.com</span>
      </div>
    </section>
    <div class="front-bottom-strip"></div>
  </article>

  <article class="card card-back">
    <div class="back-streak"></div>
    <div class="back-brand">Clearbeam Auto</div>
    <section class="pricing">
      <div class="pricing-title">Pricing</div>
      <div class="pricing-line">$25 per headlight</div>
      <div class="pricing-line">$10-$35 per scratch</div>
    </section>
  </article>

</body>
</html>
```